Web Developer Needs a Business Card Design

I need a personal business card design that represents me as a web developer for potential employers. I would like the background to be a dark color on the front for contrast with my logo and name. The back will have all my information along with a smaller version of the logo. I want something with a modern look and feel, not too conservative. This will be used for potential employers and freelance work.

Industry/Entity Type

Business

Contact Information for Business Card

Front should have my logo and name. The back should have all my personal information which would include: name: Tom Brevardi, phone: 570-614-9083, email: tombrevardi@mailwisp.com, website url: www.tombrevardi.com, logo, web developer.

Font styles to use
Sans Serif

Requirements
Must have
• Must include my logo. The color palette base color will be the logo color.

```html
<!DOCTYPE html>
<html lang="en">
<head>
<meta charset="utf-8">
<title>Tom Brevardi – Business Card</title>
<link rel="stylesheet" href="https://fonts.googleapis.com/css2?family=Lato:wght@400;700&display=swap">
<style>
  :root {
    --page-bg: #161616;
    --card-bg: #1b1311;
    --teal: #268a72;
    --teal-light: #3fb597;
    --white: #f2f2f2;
    --black: #050505;
  }
  * { margin: 0; padding: 0; box-sizing: border-box; }
  html, body { width: 1200px; height: 1086px; overflow: hidden; background: var(--page-bg); }
  body { position: relative; font-family: 'Lato', sans-serif; }

  .card {
    position: absolute; left: 254px; width: 677px; height: 386px;
    background: var(--card-bg); border-radius: 6px; overflow: hidden;
  }
  .card--front { top: 126px; }
  .card--back { top: 588px; }

  .brand { position: absolute; left: 452px; top: 39px; width: 200px; text-align: center; }
  .brand__ring { display: block; margin: 0 auto; }
  .brand__name {
    margin-top: 8px; font-weight: 700; font-size: 26px; color: var(--teal-light);
    letter-spacing: 0.2px; white-space: nowrap;
  }

  .identity__tab {
    position: absolute; left: 0; top: 196px; width: 16px; height: 48px;
    background: var(--teal); border-radius: 0 3px 3px 0;
  }
  .identity__name {
    position: absolute; left: 36px; top: 190px; font-weight: 700; font-size: 28px; color: var(--teal-light);
  }
  .identity__role {
    position: absolute; left: 36px; top: 222px; font-size: 22px; color: var(--white);
  }

  .contact { position: absolute; left: 40px; list-style: none; }
  .contact__item {
    display: flex; align-items: center; gap: 8px; height: 27px;
    font-size: 22px; color: var(--white); letter-spacing: 0.3px;
  }
  .contact__icon { width: 20px; flex: none; }
  .contact { top: 296px; }

  .web {
    position: absolute; font-size: 22px; color: var(--white); letter-spacing: 0.4px; white-space: nowrap;
  }
  .web__domain { color: var(--teal-light); }
  .web--front { right: 38px; top: 322px; }
  .web--back { left: 0; right: 0; text-align: center; top: 338px; }

  .footer-bar { position: absolute; left: 0; bottom: 0; width: 100%; height: 23px; background: var(--black); }
  .footer-bar__fill { position: absolute; left: 0; top: 0; bottom: 0; width: 574px; background: var(--teal); }
  .footer-bar__dot { position: absolute; left: 560px; top: -2px; }

  .back-mark { position: absolute; left: 246px; top: 100px; width: 188px; height: 188px; }
  .back-mark__name {
    position: absolute; inset: 0; display: flex; align-items: center; justify-content: center;
    font-weight: 700; font-size: 19px; color: var(--teal); white-space: nowrap;
  }
</style>
</head>
<body>

<section class="card card--front">
  <div class="brand">
    <svg class="brand__ring" width="104" height="104" viewBox="0 0 104 104" aria-hidden="true">
      <circle cx="52" cy="52" r="46" fill="none" stroke="var(--teal-light)" stroke-width="8"/>
    </svg>
    <div class="brand__name">TOM BREVARDI</div>
  </div>

  <div class="identity__tab"></div>
  <h1 class="identity__name">Tom Brevardi</h1>
  <p class="identity__role">President</p>

  <ul class="contact">
    <li class="contact__item">
      <svg class="contact__icon" viewBox="0 0 20 16" aria-hidden="true">
        <path d="M1 5 Q10 -1 19 5 L17 7 L14 5.5 L14 4 Q10 3 6 4 L6 5.5 L3 7 Z" fill="var(--teal-light)"/>
        <path d="M5 8 L7 6 L13 6 L15 8 L16 15 L4 15 Z" fill="var(--teal-light)"/>
        <circle cx="10" cy="10.5" r="2" fill="var(--card-bg)"/>
      </svg>
      <span>570-614-9083</span>
    </li>
    <li class="contact__item">
      <svg class="contact__icon" viewBox="0 0 20 16" aria-hidden="true">
        <rect x="0.5" y="1.5" width="19" height="13" fill="var(--teal-light)"/>
        <path d="M1 2 L10 9 L19 2 M1 14 L8 7.5 M19 14 L12 7.5" fill="none" stroke="var(--card-bg)" stroke-width="1.2"/>
      </svg>
      <span>tombrevardi@mailwisp.com</span>
    </li>
  </ul>

  <p class="web web--front">www.<span class="web__domain">tombrevardi</span>.com</p>

  <div class="footer-bar">
    <div class="footer-bar__fill"></div>
    <svg class="footer-bar__dot" width="28" height="28" viewBox="0 0 28 28" aria-hidden="true">
      <circle cx="14" cy="14" r="12" fill="var(--card-bg)" stroke="var(--teal-light)" stroke-width="2"/>
    </svg>
  </div>
</section>

<section class="card card--back">
  <div class="back-mark">
    <svg width="188" height="188" viewBox="0 0 188 188" aria-hidden="true">
      <circle cx="94" cy="94" r="86" fill="none" stroke="var(--teal)" stroke-width="14"/>
    </svg>
    <div class="back-mark__name">TOM BREVARDI</div>
  </div>
  <p class="web web--back">www.<span class="web__domain">tombrevardi</span>.com</p>
</section>

</body>
</html>
```